Quick Straightforward Billboard Redesign

- Design billboard sized for 10 foot' x 36' foot width live area size and please include bleeds 6" around all sides
- Exact blue color match is imperative in headline, logo, phone number bubble or wherever used. C-83 / M-45 / Y-1 / K-0-
- What I hope to illustrate is that our company offers the best porch screening in the area area, in regards to quality, expertise, durability, storms proof, but we do not build screen porches.
- Current board is attached below from previous designer, and as you can see sizing was off, white space on edges make it appear to be sized incorrectly.
- I also attached my own little mock up idea well well if it helps, favorite image, logo, headline, etc and ideas perhaps on expanding or making this better?

Thanks so much!

Target Market(s)

Drivers and passengers, Southeastern NC, are of immense new construction and high end homes.

Industry/Entity Type

Construction

Colors
0054AA
0677BA
7BADD7
CADEEF
E8F1F8

Requirements
Must have
• Blue color matching
Nice to have
• Design spins or other thoughts on my little mock up

```html
<!DOCTYPE html>
<html lang="en">
<head>
<meta charset="utf-8">
<title>Tidewater Screens Billboard</title>
<link rel="stylesheet" href="https://fonts.googleapis.com/css2?family=Bebas+Neue&display=swap">
<style>
  :root {
    --brand-blue: #0677BA;
    --deep-blue: #0054AA;
    --name-blue: #1a6fb5;
    --accent-green: #2fa84f;
    --call-green: #2db34a;
    --paper: #ffffff;
    --panel-white: #f4f6f8;
  }
  html, body {
    margin: 0;
    padding: 0;
    width: 1185px;
    height: 1200px;
    overflow: hidden;
    background: var(--paper);
  }
  .canvas {
    position: relative;
    width: 1185px;
    height: 1200px;
  }
  .billboard {
    position: absolute;
    left: 40px;
    top: 446px;
    width: 1105px;
    height: 307px;
    box-shadow: 0 4px 14px rgba(0,0,0,0.18);
  }
  .billboard svg { display: block; width: 100%; height: 100%; }
  .headline {
    font-family: "Bebas Neue", sans-serif;
    font-size: 118px;
    fill: var(--paper);
    letter-spacing: 2px;
  }
  .company-name {
    font-family: "Bebas Neue", sans-serif;
    font-size: 92px;
    fill: var(--name-blue);
    letter-spacing: 1px;
  }
  .phone-number {
    font-family: "Bebas Neue", sans-serif;
    font-size: 80px;
    fill: var(--paper);
    letter-spacing: 2px;
  }
</style>
</head>
<body>
<div class="canvas">
  <div class="billboard">
    <svg viewBox="0 0 1726 480" xmlns="http://www.w3.org/2000/svg">
      <defs>
        <linearGradient id="porchTones" x1="0" y1="0" x2="0" y2="1">
          <stop offset="0" stop-color="#dfeee6"/>
          <stop offset="0.3" stop-color="#e9eef0"/>
          <stop offset="0.45" stop-color="#7fb0d6"/>
          <stop offset="0.6" stop-color="#7fae5a"/>
          <stop offset="0.8" stop-color="#7a6a5a"/>
          <stop offset="1" stop-color="#c9c4bb"/>
        </linearGradient>
        <linearGradient id="greenFade" x1="0" y1="1" x2="0" y2="0">
          <stop offset="0" stop-color="var(--accent-green)"/>
          <stop offset="1" stop-color="var(--accent-green)" stop-opacity="0"/>
        </linearGradient>
        <filter id="textShadow" x="-5%" y="-20%" width="110%" height="140%">
          <feDropShadow dx="0" dy="2" stdDeviation="3" flood-color="#003a70" flood-opacity="0.6"/>
        </filter>
      </defs>

      <rect class="base-panel" x="0" y="0" width="1726" height="480" fill="var(--panel-white)"/>

      <g class="porch-photo" role="img" aria-label="Photo of a screened coastal porch with wicker seating, ceiling fan and a lake view">
        <polygon points="1030,0 1726,0 1726,480 1110,480" fill="url(#porchTones)"/>
      </g>

      <polygon class="green-slash" points="1010,300 1050,300 1110,480 1070,480" fill="url(#greenFade)"/>

      <polygon class="headline-band" points="0,0 1030,0 1112,283 0,283" fill="var(--brand-blue)"/>

      <text class="headline" x="48" y="140" filter="url(#textShadow)">SCREEN YOUR PORCH.</text>
      <text class="headline" x="48" y="245" filter="url(#textShadow)">BUILT FOR THE COAST.</text>

      <rect class="brand-square" x="50" y="360" width="66" height="66" fill="var(--brand-blue)"/>
      <text class="company-name" x="140" y="426">TIDEWATER SCREENS</text>

      <g class="call-bar">
        <rect x="1230" y="353" width="470" height="70" fill="var(--brand-blue)"/>
        <circle cx="1214" cy="388" r="56" fill="var(--call-green)" stroke="var(--paper)" stroke-width="6"/>
        <path d="M1192,362 c6,-3 10,-2 12,3 l7,14 c2,4 1,7 -3,9 l-5,3 c4,9 10,15 19,19 l3,-5 c2,-4 5,-5 9,-3 l14,7 c5,2 6,6 3,12 c-3,6 -9,10 -17,9 c-26,-4 -46,-24 -50,-50 c-1,-8 3,-14 8,-18 z" fill="var(--paper)"/>
        <text class="phone-number" x="1300" y="416">910.555.0142</text>
      </g>
    </svg>
  </div>
</div>
</body>
</html>
```